Fully digital Hybrid conversion using Photogrammetry

Bramwell Denture Solutions provides Oral surgeons, Prosthodontics, Periodontics and General Dentists Specialized service of Same day Hybrid Conversions.
We can use Analog , Conbination of Analog and digital Protocols or Fully digital Hybrid conversions.
We bring our own scanner, 3D printer and design same day of surgery if needed.
Clinician chooses Their preferd Protocol, we execute.

```html
<!DOCTYPE html>
<html lang="en">
<head>
<meta charset="utf-8">
<title>Same Day Hybrid Conversions – Bramwell Denture Solutions</title>
<link href="https://fonts.googleapis.com/css2?family=Nunito:wght@400;600;700;800;900&display=swap" rel="stylesheet">
<style>
  :root{
    --bg-deep:#0b3f9e;
    --bg-mid:#1668d0;
    --bg-light:#3d8cf0;
    --panel-soft:rgba(40,90,190,.75);
    --green:#3f9a3a;
    --green-light:#6cbf3a;
    --accent-green:#8fd33a;
    --link-blue:#6fc3ff;
    --white:#ffffff;
    --footer:#123f86;
  }
  *{box-sizing:border-box;margin:0;padding:0}
  html,body{width:1200px;height:698px;overflow:hidden}
  body{font-family:"Nunito",sans-serif;color:var(--white);background:var(--bg-deep)}
  .flyer{position:relative;width:1200px;height:698px;overflow:hidden;
    background:linear-gradient(125deg,var(--bg-deep) 0%,var(--bg-mid) 35%,var(--bg-light) 55%,var(--bg-mid) 75%,var(--bg-deep) 100%)}
  .abs{position:absolute}

  .header{left:24px;top:22px;width:1153px;height:118px;border-radius:14px 0 0 14px;
    background:linear-gradient(90deg,#1b4d97,#2a5fb0 70%,#2f6bc0);box-shadow:0 4px 10px rgba(0,0,0,.3)}
  .header h1{position:absolute;left:0;right:0;top:10px;text-align:center;white-space:nowrap;font-weight:900;font-size:59px;line-height:1;text-shadow:0 3px 4px rgba(0,0,0,.45)}
  .header p{position:absolute;left:0;right:0;top:79px;text-align:center;white-space:nowrap;font-size:26px;font-weight:600;line-height:1;text-shadow:0 2px 3px rgba(0,0,0,.4)}

  .intro-title{left:35px;top:166px;font-size:21px;font-weight:900;white-space:nowrap;text-shadow:0 2px 3px rgba(0,0,0,.4)}
  .intro-text{left:30px;top:194px;width:413px;height:109px;padding:7px 8px;border-radius:6px;white-space:nowrap;
    background:linear-gradient(90deg,var(--green) 0%,#4a9a48 60%,rgba(70,140,120,.5) 100%);
    font-size:12.2px;line-height:20px;font-weight:600}

  .panel{border-radius:10px;background:var(--panel-soft);box-shadow:0 3px 8px rgba(0,0,0,.25)}
  .photo{position:absolute;border-radius:8px;box-shadow:0 3px 6px rgba(0,0,0,.4)}

  .specialties{left:476px;top:173px;width:407px;height:91px;border-radius:6px;display:flex;
    background:linear-gradient(90deg,var(--green) 0%,var(--green-light) 70%,rgba(90,170,80,.6) 100%)}
  .specialty{flex:1;display:flex;flex-direction:column;align-items:center;padding-top:2px;border-right:1px solid rgba(255,255,255,.5);margin:6px 0}
  .specialty:last-child{border-right:none}
  .specialty svg{width:52px;height:52px}
  .specialty span{margin-top:6px;font-size:11.2px;font-weight:700;white-space:nowrap}

  .step{height:51px;border-left:1.5px solid rgba(255,255,255,.8);border-bottom:1.5px solid rgba(255,255,255,.8);
    text-align:center;font-size:10.6px;line-height:14px;font-weight:600;text-transform:uppercase;padding-top:5px;white-space:nowrap}
  .chevrons{width:90px;height:40px}

  .footer{left:22px;top:570px;width:1154px;height:118px;border-radius:10px;
    background:linear-gradient(90deg,#1a5fb4,var(--footer) 45%,#164a9b)}
  .divider{position:absolute;top:15px;width:1.5px;height:95px;background:rgba(255,255,255,.8)}
  .brand-mark{left:36px;top:28px;width:60px;height:60px;border-radius:50%;background:var(--green-light)}
  .brand-name{left:112px;top:38px;font-size:19.5px;font-weight:800;white-space:nowrap;text-transform:uppercase}
  .brand-tag{left:160px;top:68px;font-size:14.5px;letter-spacing:1.4px;white-space:nowrap}
  .find{left:506px;top:8px;font-size:18px;font-weight:900;color:var(--accent-green);white-space:nowrap}
  .person{left:506px;top:29px;font-size:19px;font-weight:800;white-space:nowrap}
  .contact{left:506px;font-size:12px;color:var(--link-blue);font-weight:600;display:flex;align-items:center;gap:7px;white-space:nowrap}
  .contact svg{width:10px;height:10px}
  .book{left:880px;top:32px;font-size:23px;font-weight:700;white-space:nowrap}
  .phone{left:878px;top:58px;font-size:30px;font-weight:800;display:flex;align-items:center;gap:10px;white-space:nowrap}
  .phone svg{width:24px;height:24px}
</style>
</head>
<body>
<main class="flyer">

  <header class="header abs">
    <h1>SAME DAY HYBRID CONVERSIONS</h1>
    <p>Powered by Photogrammetry, On-Demand Digital Design, and Proven Clinical Experience</p>
  </header>

  <h2 class="intro-title abs">FROM SCAN TO SMILE—SEAMLESSLY</h2>
  <p class="intro-text abs">By combining cutting-edge photogrammetry, on-demand digital<br>design, and years of hands-on expertise, we create a seamless and<br>precise treatment workflow. This integration allows for faster<br>turnaround, enhanced accuracy, and consistently superior<br>results—giving both clinicians and patients confidence at every stage.</p>

  <section class="panel abs" style="left:29px;top:323px;width:422px;height:171px">
    <div class="photo" role="img" aria-label="Photogrammetry scan bodies attached to implants in an open mouth"
      style="left:19px;top:20px;width:182px;height:133px;background:radial-gradient(circle at 50% 60%,#7a2a2a,#d8606a 60%,#f08a9a)"></div>
    <div class="photo" role="img" aria-label="3D printed white dental arches on a printer build plate"
      style="left:227px;top:20px;width:182px;height:133px;background:linear-gradient(150deg,#3a3a3a,#d9d4c8 45%,#1c1c1c)"></div>
  </section>

  <section class="specialties abs">
    <div class="specialty">
      <svg viewBox="0 0 50 50" fill="none" stroke="#fff" stroke-width="2"><circle cx="25" cy="25" r="23"/><path d="M17 17c3-3 6-1 8 0 2-1 5-3 8 0 2 3 0 8-1 11l-2 9-3-8-2 8-2-9c-1-3-8-7-6-11z"/></svg>
      <span>Oral Surgeons</span>
    </div>
    <div class="specialty">
      <svg viewBox="0 0 50 50" fill="none" stroke="#fff" stroke-width="2"><circle cx="25" cy="25" r="23"/><path d="M17 12c3-2 5 0 8 0s5-2 8 0c2 2 1 7-1 10H18c-2-3-3-8-1-10z"/><path d="M20 22h10M21 26h8M22 30h6M23 34h4v4h-4z"/><path d="M10 32c6-3 10 4 15 4s9-7 15-4"/></svg>
      <span>Periodontics</span>
    </div>
    <div class="specialty">
      <svg viewBox="0 0 50 50" fill="none" stroke="#fff" stroke-width="2"><circle cx="25" cy="25" r="23"/><path d="M15 14c3-3 7-1 10 0 3-1 7-3 10 0 3 3 1 9 0 12l-3 12-4-10-3 10-3-12c-1-3-10-9-7-12z"/><path d="M8 30c8 3 26 3 34 0"/></svg>
      <span>Prosthodontics</span>
    </div>
    <div class="specialty">
      <svg viewBox="0 0 50 50" fill="none" stroke="#fff" stroke-width="2"><circle cx="25" cy="25" r="23"/><path d="M15 14c3-3 7-1 10 0 3-1 7-3 10 0 3 3 1 9 0 12l-3 12-4-10-3 10-3-12c-1-3-10-9-7-12z"/><path d="M36 8v6M33 11h6"/></svg>
      <span>General Dentists</span>
    </div>
  </section>

  <section class="panel abs" style="left:478px;top:286px;width:436px;height:204px">
    <div class="photo" role="img" aria-label="CBCT scan views showing planned implant positions"
      style="left:15px;top:11px;width:148px;height:178px;background:linear-gradient(180deg,#6b4a1c,#a9a39a 40%,#2b2b2b 62%,#c7c2b8 80%,#3a2a10)"></div>
    <div class="photo" role="img" aria-label="Digital design render of a full arch prosthesis"
      style="left:182px;top:2px;width:84px;height:78px;border-radius:50%;background:radial-gradient(circle,#9aa3d8,#3d8a6a 60%,#b08650)"></div>
    <div class="photo" role="img" aria-label="Digital design render of an arch model with teeth"
      style="left:290px;top:-4px;width:98px;height:82px;border-radius:40%;background:radial-gradient(circle,#b3a06a,#3f8a60 60%,#b08650)"></div>
    <div class="photo" role="img" aria-label="Digital design render of a prosthesis with scan abutments"
      style="left:180px;top:97px;width:102px;height:97px;border-radius:30%;background:radial-gradient(circle at 50% 60%,#1fa36a,#4c9a9a 55%,#b08650)"></div>
    <div class="photo" role="img" aria-label="Digital design render of a full arch bridge on implant cylinders"
      style="left:304px;top:91px;width:120px;height:103px;border-radius:30%;background:radial-gradient(circle,#1fb07a,#2e8a7a 55%,#9a8050)"></div>
  </section>

  <section class="panel abs" style="left:933px;top:177px;width:233px;height:314px">
    <div class="photo" role="img" aria-label="Patient smile before treatment with worn teeth"
      style="left:17px;top:14px;width:188px;height:138px;background:linear-gradient(180deg,#b8a090,#a0564a 45%,#6a3a22 65%,#c07a6a)"></div>
    <div class="photo" role="img" aria-label="Patient smile after hybrid conversion"
      style="left:20px;top:167px;width:183px;height:135px;background:linear-gradient(180deg,#b8a090,#a4584c 40%,#f2ece2 60%,#b06a5a)"></div>
  </section>

  <p class="step abs" style="left:83px;top:508px;width:271px">We can use analog, combination of analog<br>and digital protocols or fully digital<br>hybrid conversions</p>
  <svg class="chevrons abs" style="left:397px;top:510px" viewBox="0 0 90 40" fill="#fff"><path d="M0 0h14l18 20-18 20H0l18-20z"/><path d="M28 0h14l18 20-18 20H28l18-20z"/><path d="M56 0h14l18 20-18 20H56l18-20z"/></svg>
  <p class="step abs" style="left:496px;top:508px;width:270px">We bring our own scanner, 3D<br>printer and design same day of surgery<br>if needed</p>
  <svg class="chevrons abs" style="left:786px;top:510px" viewBox="0 0 90 40" fill="#fff"><path d="M0 0h14l18 20-18 20H0l18-20z"/><path d="M28 0h14l18 20-18 20H28l18-20z"/><path d="M56 0h14l18 20-18 20H56l18-20z"/></svg>
  <p class="step abs" style="left:901px;top:508px;width:270px">Advanced technology &amp; expert hands<br>come together to create beautiful<br>smiles every time.</p>

  <footer class="footer abs">
    <div class="brand-mark abs"></div>
    <div class="brand-name abs">Bramwell Denture Solutions</div>
    <div class="brand-tag abs">Advanced Dental Lab Services</div>
    <div class="divider" style="left:478px"></div>
    <div class="find abs">FIND US ONLINE:</div>
    <div class="person abs">Marco Vance, Denturist MDT CDT</div>
    <div class="contact abs" style="top:56px"><svg viewBox="0 0 10 10" fill="#fff"><path d="M5 0a3.5 3.5 0 0 1 3.5 3.5C8.5 6 5 10 5 10S1.5 6 1.5 3.5A3.5 3.5 0 0 1 5 0z"/></svg>1450 Aspen Ridge Dr Suite 4 Lafayette CO 80026</div>
    <div class="contact abs" style="top:76px"><svg viewBox="0 0 10 10" fill="#fff"><rect x="0" y="2" width="10" height="7" rx="1"/></svg>mvdenturist@bramwelldenture.com</div>
    <div class="contact abs" style="top:96px"><svg viewBox="0 0 10 10" fill="none" stroke="#fff"><circle cx="5" cy="5" r="4.3"/><path d="M1 5h8M5 1c-2 2-2 6 0 8M5 1c2 2 2 6 0 8"/></svg>www.bramwelldenture.com</div>
    <div class="divider" style="left:848px"></div>
    <div class="book abs">Book an Appointment</div>
    <div class="phone abs"><svg viewBox="0 0 24 24" fill="#fff"><path d="M6.6 10.8a15 15 0 0 0 6.6 6.6l2.2-2.2c.3-.3.7-.4 1-.2 1.1.4 2.3.6 3.6.6.6 0 1 .4 1 1V20c0 .6-.4 1-1 1A17 17 0 0 1 3 4c0-.6.4-1 1-1h3.5c.6 0 1 .4 1 1 0 1.3.2 2.5.6 3.6.1.3 0 .7-.2 1z"/></svg>(555) 214-0388</div>
  </footer>

</main>
</body>
</html>
```